WordPress Website for FarShoreCrew.net

Design and create WordPress website. Detailed instructions and the exact copy and section headings for the website will be uploaded in a .pdf and .doc file. You can also access additional design elements (like alternate company logos and the chart for the cost comparison) by visiting https://qvelto.example/f/s!Xk29Lmq7Rt-pWz3HNv8cQYbDkua

Target Market(s)

The website is geared toward either entrepreneurs (or solopreneurs) and small- to medium-sized companies in the United States (with anywhere from 1 to 250 employees) who want to hire people living in the Philippines to work remotely. Common clients include real estate agents or other people who want to hire a virtual assistant. However, we provide remote professionals for all jobs, in all industries.

Coding

Requirements
Must have
• The website MUST have a TalkPane widget in the bottom-right-corner of every page.
• The website MUST be responsive and optimized for mobile devices like iPads and cellphones.
• The website should follow the colors in our logo. The colors of our logo are: CMYK (78.5, 31.61, 1.15, 0) and (89.3, 83.2, 4.28, 0.32)
• If you include pictures of people, they should look like Filipinos. They should NOT look like call center representatives; and they should NOT be wearing headsets. If you include pictures of people, there should be a cross section of people: mature people, middle-age people; and both men and women. The typical people are virtual assistants, bookkeepers, HR administrators.
Nice to have
• It would be NICE to have animated icons or gifs, like the ones at www.gantrovia.com (next to the words Virtual Assistants, Website Maintenance, and Virtual Bookkeeping).

```html
<!DOCTYPE html>
<html lang="en">
<head>
<meta charset="utf-8">
<title>FarShoreCrew.net</title>
<link rel="stylesheet" href="https://fonts.googleapis.com/css2?family=Nunito+Sans:wght@300;400;600;700;800&display=swap">
<style>
:root{
  --sky:#2f9fe8;
  --royal:#3a35e6;
  --ink:#2b2f38;
  --muted:#8b919c;
  --paper:#ffffff;
  --mist:#f3f4f6;
  --line:#e3e5ea;
  --night:#1f2430;
  --hero-a:#3d6f8f;
  --hero-b:#b7c9d3;
}
*{box-sizing:border-box;margin:0;padding:0}
html,body{width:1200px;height:5356px;overflow:hidden}
body{position:relative;font-family:"Nunito Sans",Arial,sans-serif;color:var(--ink);background:var(--paper)}
section,footer{position:relative;width:1200px;overflow:hidden}
h2.section-title{position:absolute;left:0;width:100%;font-weight:400;font-size:34px;text-align:center;color:var(--ink)}
.btn{display:inline-block;padding:12px 26px;font-size:13px;font-weight:600;border-radius:3px}

/* hero */
.hero{height:660px;color:#fff}
.hero-photo{position:absolute;inset:0;background:linear-gradient(100deg,var(--hero-a) 0%,#6f97ad 45%,var(--hero-b) 75%,#d88a6f 100%)}
.hero-shade{position:absolute;inset:0;background:rgba(20,40,60,.35)}
.nav{position:absolute;top:22px;left:0;width:100%;height:40px}
.brand{position:absolute;left:60px;top:6px;display:flex;align-items:center;gap:8px;font-weight:700;font-size:17px;color:var(--sky)}
.brand i{display:block;width:14px;height:14px;background:var(--sky)}
.nav-links{position:absolute;left:490px;top:10px;display:flex;gap:36px;font-size:13px;font-weight:600}
.nav-links span:first-child{border-bottom:2px solid #fff;padding-bottom:3px}
.hero-title{position:absolute;top:170px;left:0;width:100%;text-align:center;font-size:30px;font-weight:400;line-height:1.25}
.hero-sub{position:absolute;top:250px;left:0;width:100%;text-align:center;font-size:13px;line-height:1.5;opacity:.9}
.hero .btn{position:absolute;top:334px;left:532px;background:var(--sky);color:#fff}

/* team */
.team{height:700px}
.team .section-title{top:30px}
.team-photos{position:absolute;top:100px;left:60px;width:1080px;height:540px;display:flex;gap:16px}
.team-photos div{flex:1;background:linear-gradient(180deg,#9aa4ad,#5c646d)}

/* why */
.why{height:420px;background:var(--mist)}
.why .section-title{top:30px}
.why-sub{position:absolute;top:86px;left:300px;width:600px;text-align:center;font-size:13px;line-height:1.6;color:var(--muted)}
.features{position:absolute;top:150px;left:120px;width:960px;display:flex;justify-content:space-between}
.feature{width:280px;text-align:center}
.feature svg{width:34px;height:34px}
.feature h3{font-size:14px;font-weight:700;margin:10px 0 8px}
.feature p{font-size:12px;line-height:1.6;color:var(--muted)}
.dots{position:absolute;top:290px;left:0;width:100%;display:flex;justify-content:center;gap:8px}
.dots i{width:7px;height:7px;border-radius:50%;background:#c8ccd3}
.dots i.on{background:var(--sky)}

/* clients */
.clients{height:332px}
.clients .section-title{top:88px}
.client-row{position:absolute;top:172px;left:170px;width:860px;display:flex;justify-content:space-between;align-items:center}
.client-name{display:flex;align-items:center;gap:8px;font-size:26px;font-weight:700;color:#555a63}
.client-name i{display:block;width:14px;height:14px;border-radius:50%;background:#555a63}

/* pricing */
.pricing{height:1240px;background:var(--mist)}
.pricing .pricing-title{top:60px}
.rate{position:absolute;top:140px;left:130px;width:240px;text-align:center;color:var(--sky)}
.rate b{display:block;font-size:120px;font-weight:800;line-height:1.1}
.rate span{display:block;font-size:17px;font-weight:800;color:var(--ink);margin-top:4px}
.rate-copy{position:absolute;top:150px;left:400px;width:660px;font-size:13px;line-height:1.7;color:var(--muted)}
.rate-copy p+p{margin-top:14px}
.pricing .compare-title{top:432px}
.card{position:absolute;background:#fff;box-shadow:0 6px 24px rgba(0,0,0,.12);padding:30px 32px}
.card.onsite{top:628px;left:300px;width:280px;height:540px;border-top:4px solid var(--sky)}
.card.remote{top:528px;left:620px;width:292px;height:660px;padding-top:0}
.card-flag{margin:0 -32px 24px;height:30px;background:var(--royal);color:#fff;font-size:11px;font-weight:700;padding:8px 20px}
.card h4{font-size:24px;font-weight:400;color:var(--sky);line-height:1.15}
.card .salary{font-size:26px;color:var(--sky);margin:8px 0 18px}
.card .salary small{font-size:11px;color:var(--muted)}
.card p{font-size:11px;line-height:1.5;color:var(--ink);padding:10px 0;border-bottom:1px solid var(--line)}
.card h5{font-size:20px;font-weight:400;color:var(--sky);margin:20px 0 8px}
.card .btn{margin-top:24px;background:var(--sky);color:#fff;padding:9px 20px;font-size:11px}

/* industries */
.industries{height:688px}
.industries .section-title{top:220px}
.ind-text{position:absolute;top:356px;left:140px;width:360px}
.tag{display:inline-block;background:var(--sky);color:#fff;font-size:17px;padding:8px 16px}
.ind-text h3{font-size:17px;font-weight:600;color:var(--sky);margin:12px 0 16px}
.ind-text p{font-size:12px;line-height:1.6;color:var(--muted)}
.ind-visual{position:absolute;top:300px;left:640px;width:420px;height:340px}
.ind-visual .blk{position:absolute;background:var(--royal)}
.ind-visual .photo{position:absolute;left:20px;top:20px;width:380px;height:300px;background:linear-gradient(135deg,#d6c7b4,#9a7f6b 55%,#c24b3a)}

/* getting started */
.started{height:740px;background:var(--mist)}
.started .section-title{top:100px}
.steps{position:absolute;top:256px;left:200px;width:800px;display:flex;justify-content:space-between}
.step{width:220px;text-align:center}
.step svg{width:34px;height:34px}
.step h3{font-size:13px;font-weight:600;margin:12px 0 10px}
.step p{font-size:11px;line-height:1.7;color:var(--muted)}

/* call now */
.callnow{height:540px;background:var(--mist)}
.callnow svg.wave{position:absolute;inset:0}
.callnow .section-title{top:118px;color:#fff}
.call-copy{position:absolute;top:176px;left:280px;width:640px;text-align:center;font-size:12px;line-height:1.6;color:#e6e5ff}
.callnow .btn{position:absolute;top:330px;left:553px;border:1px solid #fff;color:#fff}

/* footer */
.site-footer{height:36px;background:var(--night);color:#8a90a0;font-size:10px;padding:12px 60px}

/* chat widget */
.chat{position:absolute;right:40px;bottom:0;width:160px}
.chat .status{display:inline-block;margin:0 0 10px 36px;background:#fff;color:var(--ink);font-size:10px;padding:5px 12px;border-radius:12px;box-shadow:0 2px 8px rgba(0,0,0,.2)}
.chat .bar{height:26px;background:var(--royal);color:#fff;font-size:11px;font-weight:700;padding:6px 14px;border-radius:4px 4px 0 0}
</style>
</head>
<body>

<section class="hero">
  <div class="hero-photo" role="img" aria-label="Photo of a smiling young professional working at a laptop in a bright office"></div>
  <div class="hero-shade"></div>
  <nav class="nav">
    <div class="brand"><i></i>FarShoreCrew.net</div>
    <div class="nav-links"><span>Home</span><span>About</span><span>Jobs</span><span>Contact</span></div>
  </nav>
  <h1 class="hero-title">Intelligent, Educated, Loyal, Hard-Working Employees In Emerging<br>Economies…Doing The Same Jobs Better And For Far Less Money.</h1>
  <p class="hero-sub">We recruit your ideal teammate, then manage payroll and support so you can focus on growth.<br>Hiring full-time talent abroad saves up to 70% compared with a local hire.</p>
  <span class="btn">Get A Consultation</span>
</section>

<section class="team">
  <h2 class="section-title">Meet Our Remote Professionals</h2>
  <div class="team-photos">
    <div role="img" aria-label="Portrait photo of a remote professional"></div>
    <div role="img" aria-label="Portrait photo of a remote professional"></div>
    <div role="img" aria-label="Portrait photo of a remote professional"></div>
    <div role="img" aria-label="Portrait photo of a remote professional"></div>
  </div>
</section>

<section class="why">
  <h2 class="section-title">Why Choose Us ?</h2>
  <p class="why-sub">You've always wanted to hire smart, dependable staff, but the cost held you back.<br>Our team makes that possible for every business, big or small.</p>
  <div class="features">
    <div class="feature">
      <svg viewBox="0 0 34 34" fill="none" stroke="#2f9fe8" stroke-width="2"><path d="M6 20a11 11 0 0 1 22 0"/><path d="M4 22h26M10 26h14"/></svg>
      <h3>Continuity</h3>
      <p>Your team stays with you for years, keeping knowledge<br>and momentum inside your business.</p>
    </div>
    <div class="feature">
      <svg viewBox="0 0 34 34" fill="none" stroke="#2f9fe8" stroke-width="2"><path d="M17 4l4 8.5 9 1.2-6.6 6.3 1.7 9L17 24.6 8.9 29l1.7-9L4 13.7l9-1.2z"/></svg>
      <h3>Caliber</h3>
      <p>We hire degree holders with proven skills, strong<br>English and a record of quality work.</p>
    </div>
    <div class="feature">
      <svg viewBox="0 0 34 34" fill="none" stroke="#2f9fe8" stroke-width="2"><path d="M17 4l11 4v8c0 7-5 12-11 14C11 28 6 23 6 16V8z"/><path d="M12 17l4 4 7-8"/></svg>
      <h3>Security</h3>
      <p>Secure systems, signed agreements and monitored<br>access protect your data every day.</p>
    </div>
  </div>
  <div class="dots"><i class="on"></i><i></i><i></i></div>
</section>

<section class="clients">
  <h2 class="section-title">Companies That Trust Us</h2>
  <div class="client-row">
    <div class="client-name"><i></i>Brightmint</div>
    <div class="client-name"><i></i>Fizzwell</div>
    <div class="client-name"><i></i>Harlow Motor Works</div>
  </div>
</section>

<section class="pricing">
  <h2 class="section-title pricing-title">Pricing</h2>
  <div class="rate"><b>$10</b><span>PER HOUR</span></div>
  <div class="rate-copy">
    <p>Almost all of our remote professionals cost only $10 per hour. That's less than the minimum wage in many states and includes everything you need: salary, benefits, taxes, equipment and our ongoing support. There are no setup fees, no recruiting fees and no long contracts, so you can start small and grow at your own pace.</p>
    <p>You don't pay for overhead like office space or computers. You don't pay for recruiting or training. You only pay for the hours your remote professional works, and we handle the rest. Best of all, your team is already trained and ready to help on day one.</p>
  </div>
  <h2 class="section-title compare-title">Cost Comparison</h2>

  <div class="card onsite">
    <h4>ON-SITE</h4>
    <div class="salary">$ 76,960 <small>/ Per Year Salary</small></div>
    <p>Hours – $37 / Hour</p>
    <p>Benefits – $2,664 / Month</p>
    <p>Taxes – $8,300 / Year</p>
    <h5>Benefits @ 35%</h5>
    <p>Health, Dental, Life Insurance, Retirement, Pension Plans, 401k = $2,664 / Year</p>
    <h5>Taxes &amp; Overheads</h5>
    <p>Taxes – $8,300 / Year</p>
  </div>

  <div class="card remote">
    <div class="card-flag">Recommended</div>
    <h4>REMOTE<br>PROFESSIONAL</h4>
    <div class="salary">$ 20,800 <small>/ Per Year Salary</small></div>
    <p>Hours – $10 / Hour</p>
    <p>Benefits – $1,733 / Month</p>
    <p>Taxes – $0 / Year</p>
    <h5>Benefits @ 35%</h5>
    <p>Health, Dental, Life Insurance, Retirement, Pension Plans, 401k = $0 / Year</p>
    <h5>Taxes &amp; Overheads</h5>
    <p>Taxes – $0 / Year</p>
    <span class="btn">Sign Up Now</span>
  </div>
</section>

<section class="industries">
  <h2 class="section-title">Industries/Services</h2>
  <div class="ind-text">
    <span class="tag">We're Not Just Virtual Assistants</span>
    <h3>We Have People For All Jobs, In All Industries.</h3>
    <p>If it can be done with a computer or a phone, we have a remote professional ready to do it for you. From bookkeeping and customer care to design, research and HR support, we match you with the right person and manage the details so your business keeps moving forward.</p>
  </div>
  <div class="ind-visual">
    <div class="blk" style="left:0;top:0;width:70px;height:70px"></div>
    <div class="blk" style="right:0;top:40px;width:50px;height:50px"></div>
    <div class="blk" style="left:60px;bottom:0;width:40px;height:40px"></div>
    <div class="blk" style="right:10px;bottom:0;width:60px;height:60px"></div>
    <div class="photo" role="img" aria-label="Photo of a professional working at a desk in a modern office"></div>
  </div>
</section>

<section class="started">
  <h2 class="section-title">Getting Started</h2>
  <div class="steps">
    <div class="step">
      <svg viewBox="0 0 34 34" fill="none" stroke="#2f9fe8" stroke-width="2"><path d="M5 7h24v16H14l-6 5v-5H5z"/></svg>
      <h3>Tell us what you need</h3>
      <p>Share the role, skills and hours you want. We review your goals and build a clear plan for the right remote hire.</p>
    </div>
    <div class="step">
      <svg viewBox="0 0 34 34" fill="none" stroke="#2f9fe8" stroke-width="2"><circle cx="17" cy="12" r="6"/><path d="M6 30c1-6 6-9 11-9s10 3 11 9"/></svg>
      <h3>Meet and approve your assistant</h3>
      <p>Interview our shortlist of qualified candidates and choose the one you like best. We handle onboarding, contracts and setup so your new teammate starts quickly and smoothly.</p>
    </div>
    <div class="step">
      <svg viewBox="0 0 34 34" fill="none" stroke="#2f9fe8" stroke-width="2"><path d="M17 4c6 4 8 10 6 18h-12C9 14 11 8 17 4z"/><path d="M11 22l-4 6h6M23 22l4 6h-6"/></svg>
      <h3>Launch and Track</h3>
      <p>Your remote professional gets to work and you track progress with simple reports and regular check-ins from us.</p>
    </div>
  </div>
</section>

<section class="callnow">
  <svg class="wave" viewBox="0 0 1200 540" preserveAspectRatio="none" aria-hidden="true">
    <path d="M0 30 C200 -20 380 70 600 30 S1000 -20 1200 30 V540 H0z" fill="#6b66f2" opacity=".6"/>
    <path d="M0 60 C220 10 420 100 640 55 S1020 10 1200 60 V540 H0z" fill="#3a35e6"/>
  </svg>
  <h2 class="section-title">Call Now</h2>
  <p class="call-copy">Give us a call now. We're happy to answer all your questions. We will get to know more about your business and help you find the right remote professional. If the time difference worries you, don't be. Our team works your hours and reports daily. Many clients start with a single hire and grow to a full team within months. Call today and take the first step.</p>
  <span class="btn">Call Now</span>
</section>

<footer class="site-footer">© 2024 FarShoreCrew.net. All rights reserved.</footer>

<div class="chat">
  <span class="status">We are offline</span>
  <div class="bar">Chat With Us</div>
</div>

</body>
</html>
```